Re-Design of existing Shopwise Website

Hi,

We are looking for a skilled person to work with us on improving the design of our website to make it more user friendly. We are a Makeup brush and makeup accessories company and our current website can be viewed at pillowandfern dot com.We are looking to simplify the layout and make it more modern and mobile friendly.

We have designs in mind which we would like to implement to our site which we feel would work better for us to increase traffic and sales.

We would like the layout to have clear sections for brushes,lashes ,sponge and also our tutorials on the landing page.

Industry/Entity Type

Hair And Beauty

Number of Pages Required

5+ page

Font styles to use
Sans Serif

Colors
b8a6cd
d3a5cc
eea4c8
ffffff
000000

Requirements
Must have
• -Clear ,modern landing page.
• -easy navigation
• -simple design
• -professional design approach
Nice to have
• cross selling pop up
Should not have
• over use of bold colour.

```html
<!DOCTYPE html>
<html lang="en">
<head>
<meta charset="utf-8">
<title>Pillow&amp;Fern</title>
<link href="https://fonts.googleapis.com/css2?family=Titillium+Web:wght@200;300;400&display=swap" rel="stylesheet">
<style>
  :root {
    --black: #000000;
    --white: #ffffff;
    --pink: #d77fb4;
    --rose: #b8739f;
    --grey: #9d9d9d;
    --slate: #5a5a5a;
    --muted: #a8a8a8;
    --footer-text: #b5b5b5;
  }
  * { margin: 0; padding: 0; box-sizing: border-box; }
  html, body { width: 1200px; height: 1200px; overflow: hidden; background: var(--black); }
  body { font-family: "Titillium Web", sans-serif; color: var(--white); position: relative; }

  .hero { position: absolute; left: 0; top: 0; width: 1200px; height: 712px; background: var(--black); overflow: hidden; }
  .hero__photo {
    position: absolute; left: 0; top: 0; width: 900px; height: 712px;
    background:
      linear-gradient(90deg, rgba(0,0,0,0) 0%, rgba(0,0,0,0) 55%, rgba(0,0,0,0.85) 82%, #000 100%),
      radial-gradient(ellipse at 38% 38%, #e3b39a 0%, #b9744f 28%, #6e4326 52%, #3f4a22 75%, #1d2410 100%);
  }
  .brand { position: absolute; left: 748px; top: 270px; font-weight: 200; font-size: 62px; letter-spacing: 1px; color: var(--pink); line-height: 1; }
  .main-nav { position: absolute; left: 835px; top: 400px; list-style: none; }
  .main-nav li { font-size: 14px; font-weight: 300; height: 30px; line-height: 30px; text-transform: uppercase; display: flex; align-items: center; }
  .main-nav .caret { margin-left: 12px; width: 0; height: 0; border-left: 4.5px solid transparent; border-right: 4.5px solid transparent; border-top: 8px solid var(--pink); }

  .tile { position: absolute; width: 600px; height: 188px; overflow: hidden; }
  .tile__label { position: absolute; font-weight: 200; text-transform: uppercase; line-height: 1; }

  .tile--products { left: 0; top: 712px; background: var(--white); }
  .tile--products .tile__photo { position: absolute; left: 398px; top: 10px; width: 140px; height: 178px; background: linear-gradient(180deg, #d9d2cc 0%, #c95aa6 45%, #d06fb0 100%); border-radius: 4px 4px 0 0; opacity: .85; }
  .tile--products .tile__label { left: 37px; top: 122px; font-size: 40px; color: var(--muted); }

  .tile--tutorials { left: 600px; top: 712px; background: linear-gradient(120deg, #c886b1 0%, #a8628f 55%, #c98aae 100%); }
  .tile--tutorials .tile__label { left: 51px; top: 122px; font-size: 40px; color: var(--white); }

  .tile--social { left: 0; top: 900px; height: 187px; background: linear-gradient(135deg, #6c6c6c 0%, #4e4e4e 55%, #5f5f5f 100%); }
  .social-mark { position: absolute; left: 33px; top: 113px; width: 38px; height: 38px; border: 4px solid var(--white); border-radius: 10px; }
  .social-kicker { position: absolute; left: 91px; top: 94px; font-size: 20px; font-weight: 300; text-transform: uppercase; line-height: 1; }
  .social-name { position: absolute; left: 89px; top: 113px; font-size: 40px; font-weight: 200; text-transform: uppercase; line-height: 1; }

  .tile--newsletter { left: 600px; top: 900px; height: 187px; background: var(--grey); }
  .newsletter__kicker { position: absolute; left: 37px; top: 82px; font-size: 19px; font-weight: 300; text-transform: uppercase; line-height: 1; }
  .newsletter__title { position: absolute; left: 35px; top: 100px; font-size: 40px; font-weight: 200; text-transform: uppercase; line-height: 1; }
  .newsletter__note { position: absolute; left: 36px; top: 146px; font-size: 11px; font-weight: 300; }
  .newsletter__field { position: absolute; left: 305px; top: 95px; width: 263px; height: 59px; background: var(--white); border-radius: 3px; }
  .newsletter__field svg { position: absolute; right: 20px; top: 20px; }

  .site-footer { position: absolute; left: 0; top: 1087px; width: 1200px; height: 113px; background: var(--black); font-size: 12px; font-weight: 300; color: var(--footer-text); }
  .footer-links { position: absolute; left: 33px; top: 52px; }
  .footer-copy { position: absolute; right: 38px; top: 52px; }
</style>
</head>
<body>
  <header class="hero">
    <div class="hero__photo" role="img" aria-label="Portrait of a young woman with auburn braids lying in grass, wearing makeup"></div>
    <div class="brand">PILLOW&amp;FERN</div>
    <ul class="main-nav">
      <li>Luxury Silk Lashes</li>
      <li>Deluxe Lashes</li>
      <li>Individual Brushes</li>
      <li>Brush Sets</li>
      <li>Clearance</li>
      <li>Tutorials<span class="caret"></span></li>
      <li>Softtouch Sponge<span class="caret"></span></li>
    </ul>
  </header>

  <section class="tile tile--products">
    <div class="tile__photo" role="img" aria-label="Four pink-handled makeup brushes"></div>
    <h2 class="tile__label">New Products</h2>
  </section>

  <section class="tile tile--tutorials" role="img" aria-label="Hand holding an eyeshadow palette with a pink overlay">
    <h2 class="tile__label">Make Up Tutorials</h2>
  </section>

  <section class="tile tile--social" role="img" aria-label="Flat lay of makeup brushes, mascara wand and eyelash curler">
    <span class="social-mark"></span>
    <span class="social-kicker">Follow us on</span>
    <span class="social-name">Snapfeed</span>
  </section>

  <section class="tile tile--newsletter">
    <span class="newsletter__kicker">Subscribe to our</span>
    <span class="newsletter__title">Newsletter</span>
    <span class="newsletter__note">Be the first to know about new products and sales</span>
    <div class="newsletter__field">
      <svg width="20" height="18" viewBox="0 0 20 18"><path d="M0 8 L20 0 L15 18 L9 12 Z" fill="#c26ea3"/><path d="M9 12 L20 0 L8 17 Z" fill="#a65489"/></svg>
    </div>
  </section>

  <footer class="site-footer">
    <div class="footer-links">Luxury Silk Lashes | Deluxe Lashes | Individual Brushes | Brush Sets | Clearance | Tutorials | Softtouch Sponge</div>
    <div class="footer-copy">© 2018, Pillow&amp;Fern. Powered by Shopwise</div>
  </footer>
</body>
</html>
```